BrookvaleLogic Website Design

To design a website for BrookvaleLogic, a software development company. The website should reflect the branding of our company, which is Smart, Beautiful, and Sophisticated. The existing website is www.brookvalelogic-example.com.sg

```html
<!DOCTYPE html>
<html lang="en">
<head>
<meta charset="utf-8">
<title>BrookvaleLogic</title>
<link href="https://fonts.googleapis.com/css2?family=Open+Sans:wght@400;600&family=Montserrat:wght@500&display=swap" rel="stylesheet">
<style>
  :root {
    --text: #3a3a3a;
    --muted: #777;
    --link: #1a73c8;
    --accent-red: #d9382b;
    --brand: #1b6fa8;
    --band: rgba(24, 102, 152, 0.93);
    --navy-1: #123f66;
    --navy-2: #0d3559;
    --navy-3: #0b4a6c;
    --sky-light: #a6c9ef;
    --sky-mid: #5b97d1;
    --slate: #6a84b6;
    --cyan: #5db7e3;
    --locate: #0e4468;
    --photo-1: #c9c4bc;
    --photo-2: #b98d78;
    --photo-3: #c7c1b8;
  }
  * { box-sizing: border-box; margin: 0; padding: 0; }
  html, body { width: 1200px; height: 835px; overflow: hidden; background: #fff; }
  body { font-family: "Open Sans", Arial, sans-serif; color: var(--text); position: relative; }

  .brand { position: absolute; left: 141px; top: 22px; display: flex; align-items: center; gap: 12px; }
  .brand-dot { width: 44px; height: 44px; border-radius: 50%; background: var(--brand); }
  .brand-name { font-family: "Open Sans", Arial, sans-serif; font-size: 30px; font-weight: 400; color: var(--brand); letter-spacing: 0.2px; }

  .main-nav { position: absolute; right: 141px; top: 17px; text-align: right; font-size: 13.5px; line-height: 28px; }
  .main-nav ul { list-style: none; }
  .main-nav li { display: inline; }
  .main-nav li + li::before { content: "|"; color: #c8c8c8; margin: 0 8px; }
  .main-nav a { color: #444; text-decoration: none; }

  .feature { position: absolute; left: 141px; width: 459px; overflow: hidden; }
  .feature .photo { position: absolute; inset: 0; }
  .feature .band {
    position: absolute; left: 0; right: 0; bottom: 0; height: 51px;
    background: var(--band); color: #fff;
    font-family: "Montserrat", Arial, sans-serif; font-weight: 500; font-size: 16px;
    letter-spacing: 0.4px; text-transform: uppercase;
    display: flex; align-items: center; padding: 0 19px;
  }
  .feature .band.right { justify-content: flex-end; gap: 20px; }
  .slider { top: 100px; height: 233px; }
  .society { top: 342px; height: 215px; }
  .hiring { top: 566px; height: 215px; }
  .slide-arrow { position: absolute; top: 102px; }
  .slide-arrow.prev { left: 9px; }
  .slide-arrow.next { right: 9px; }

  .tile {
    position: absolute; width: 221px; height: 163px; color: #fff; text-decoration: none;
    font-family: "Montserrat", Arial, sans-serif; font-weight: 500; font-size: 15.5px;
    letter-spacing: 0.4px; text-transform: uppercase;
  }
  .tile span { position: absolute; left: 8px; bottom: 8px; }
  .col-a { left: 609px; }
  .col-b { left: 839px; }
  .row-1 { top: 100px; }
  .row-2 { top: 273px; }
  .row-3 { top: 445px; }
  .row-4 { top: 618px; }
  .t-story { background: var(--navy-1); }
  .t-profile { background: var(--sky-light); }
  .t-mission { background: var(--sky-mid); }
  .t-team { background: var(--navy-2); }
  .t-board { background: var(--navy-3); }
  .t-products { background: var(--slate); }
  .t-contact { background: var(--cyan); }
  .t-locate { background: var(--locate); }

  .site-footer { position: absolute; left: 141px; right: 141px; top: 812px; font-size: 13.5px; display: flex; justify-content: space-between; }
  .site-footer .owner { color: var(--link); }
  .site-footer .rights { color: var(--muted); }
  .site-footer .credit { color: var(--accent-red); }
</style>
</head>
<body>
  <header>
    <div class="brand">
      <div class="brand-dot"></div>
      <div class="brand-name">BrookvaleLogic</div>
    </div>
    <nav class="main-nav">
      <ul>
        <li><a href="#">Our Story</a></li><li><a href="#">Company Profile</a></li><li><a href="#">Mission and Vision</a></li><li><a href="#">The Team</a></li><li><a href="#">Board of Director</a></li>
      </ul>
      <ul>
        <li><a href="#">Product and Services</a></li><li><a href="#">Giving Back to Society</a></li><li><a href="#">We are Hiring</a></li><li><a href="#">Contact us</a></li><li><a href="#">Locate us</a></li>
      </ul>
    </nav>
  </header>

  <main>
    <section class="feature slider">
      <div class="photo" role="img" aria-label="Photo of a team working together at a computer in a bright office" style="background:linear-gradient(135deg,#e4e2dc,var(--photo-1) 60%,#a9a39a)"></div>
      <svg class="slide-arrow prev" width="29" height="29" viewBox="0 0 29 29"><circle cx="14.5" cy="14.5" r="13.5" fill="rgba(255,255,255,.85)" stroke="#999"/><path d="M16.5 9.5l-5 5 5 5" fill="none" stroke="#777" stroke-width="1.4"/></svg>
      <svg class="slide-arrow next" width="29" height="29" viewBox="0 0 29 29"><circle cx="14.5" cy="14.5" r="13.5" fill="rgba(255,255,255,.85)" stroke="#999"/><path d="M12.5 9.5l5 5-5 5" fill="none" stroke="#777" stroke-width="1.4"/></svg>
      <div class="band">We develop software and application that ...</div>
    </section>

    <a class="feature society" href="#">
      <div class="photo" role="img" aria-label="Photo of volunteers handing out papers at a community event" style="background:linear-gradient(135deg,#d9cfc6,var(--photo-2) 55%,#8f6e60)"></div>
      <div class="band right">Giving back to society
        <svg width="26" height="26" viewBox="0 0 26 26"><circle cx="13" cy="13" r="11.5" fill="none" stroke="#fff" stroke-width="1.6"/><path d="M7 13h11M14 8.5l4.5 4.5-4.5 4.5" fill="none" stroke="#fff" stroke-width="1.8"/></svg>
      </div>
    </a>

    <a class="feature hiring" href="#">
      <div class="photo" role="img" aria-label="Photo of a smiling new hire standing in a busy open office" style="background:linear-gradient(135deg,#eeece8,var(--photo-3) 60%,#9c9a98)"></div>
      <div class="band right">We are hiring
        <svg width="26" height="26" viewBox="0 0 26 26"><circle cx="13" cy="13" r="11.5" fill="none" stroke="#fff" stroke-width="1.6"/><path d="M7 13h11M14 8.5l4.5 4.5-4.5 4.5" fill="none" stroke="#fff" stroke-width="1.8"/></svg>
      </div>
    </a>

    <a class="tile col-a row-1 t-story" href="#" role="img" aria-label="Tinted photo of colleagues meeting"><span>Our Story</span></a>
    <a class="tile col-b row-1 t-profile" href="#"><span>Company Profile</span></a>
    <a class="tile col-a row-2 t-mission" href="#"><span>Mission and Vision</span></a>
    <a class="tile col-b row-2 t-team" href="#" role="img" aria-label="Tinted group photo of the team"><span>The Team</span></a>
    <a class="tile col-a row-3 t-board" href="#" role="img" aria-label="Tinted photo of a boardroom handshake"><span>Board of Director</span></a>
    <a class="tile col-b row-3 t-products" href="#"><span>Product &amp; Services</span></a>
    <a class="tile col-a row-4 t-contact" href="#"><span>Contact Us</span></a>
    <a class="tile col-b row-4 t-locate" href="#" role="img" aria-label="Tinted street map of the office area"><span>Locate Us</span></a>
  </main>

  <footer class="site-footer">
    <div>Copyright © 2014 <span class="owner">BrookvaleLogic.</span> <span class="rights">All rights reserved.</span></div>
    <div class="credit">NorthQuay Studio</div>
  </footer>
</body>
</html>
```